" Consultório de pediatria geral onde 3 médicos atendem. Eu, meu irmão e meu pai. Atendemos de recém-nascidos até adolescentes. Também faço atendimento na sala de parto e vacinas. "

```html
<!DOCTYPE html>
<html lang="pt-BR">
<head>
<meta charset="utf-8">
<title>Receituário – Moravel Pediatria</title>
<link rel="stylesheet" href="https://fonts.googleapis.com/css2?family=Marcellus&family=Open+Sans:wght@400;600&display=swap">
<style>
  :root{
    --bg:#e4e4e6;
    --paper:#ffffff;
    --blue:#2f4fa8;
    --blue-dark:#23408f;
    --blue-light:#3d6cc4;
    --teal:#1eb0a2;
    --bar-text:#d9d4ff;
    --watermark:#f1f1f3;
  }
  *{margin:0;padding:0;box-sizing:border-box}
  html,body{width:1200px;height:1200px;overflow:hidden;background:var(--bg)}
  .sheet{
    position:absolute;left:204px;top:48px;width:792px;height:1105px;
    background:var(--paper);overflow:hidden;
  }
  .brand{
    position:absolute;top:33px;left:0;width:100%;
    display:flex;flex-direction:column;align-items:center;
  }
  .brand-dot{width:56px;height:56px;border-radius:50%;background:var(--teal)}
  .brand-name{
    margin-top:6px;font-family:"Marcellus",serif;font-size:30px;
    color:var(--blue);letter-spacing:1px;line-height:1;
  }
  .brand-tag{
    margin-top:3px;font-family:"Marcellus",serif;font-size:12px;
    color:var(--teal);letter-spacing:5px;line-height:1;
  }
  .title-bar{
    position:absolute;left:53px;top:181px;width:686px;height:28px;
    background:var(--blue);border-bottom:4px solid var(--teal);
    display:flex;align-items:center;justify-content:center;
    font-family:"Marcellus",serif;font-size:15px;color:var(--bar-text);letter-spacing:.5px;
  }
  .watermark{
    position:absolute;left:474px;top:705px;width:252px;height:252px;
    border-radius:50%;background:var(--watermark);
  }
  .footer{
    position:absolute;left:0;bottom:34px;width:100%;height:50px;
    background:linear-gradient(90deg,var(--blue-dark),var(--blue-light));
    font-family:"Open Sans",sans-serif;font-size:11px;color:#e8ecf8;
  }
  .contact{position:absolute;top:0;height:100%;display:flex;align-items:center;gap:12px}
  .contact svg{width:18px;height:18px;fill:#e8ecf8}
  .contact.phone{left:128px}
  .contact.mail{left:286px}
  .contact.address{left:506px;line-height:1.2}
</style>
</head>
<body>
  <main class="sheet">
    <header class="brand">
      <div class="brand-dot"></div>
      <div class="brand-name">MORAVEL</div>
      <div class="brand-tag">PEDIATRIA</div>
    </header>

    <div class="title-bar">RECEITUÁRIO</div>

    <div class="watermark"></div>

    <footer class="footer">
      <div class="contact phone">
        <svg viewBox="0 0 24 24"><path d="M3 8c0-2 3-4 9-4s9 2 9 4v2h-5V8.5c-1-.5-2.5-.7-4-.7s-3 .2-4 .7V10H3zM6 12h12l2 7H4z"/></svg>
        <span>(11) 1234-5678</span>
      </div>
      <div class="contact mail">
        <svg viewBox="0 0 24 24"><path d="M3 6h18v12H3zM4.5 7.5 12 13l7.5-5.5z" fill-rule="evenodd"/></svg>
        <span>seuemail@email.com.br</span>
      </div>
      <div class="contact address">
        <svg viewBox="0 0 24 24"><path d="M12 3 2 12h3v8h5v-5h4v5h5v-8h3z"/></svg>
        <span>Endereço Completo<br>Cidade - Estado - Cep</span>
      </div>
    </footer>
  </main>
</body>
</html>
```